Calendar Ad / Flyer

Our law firm needs a calendar ad to place in a local calendar.
THE DEADLINE IS THIS THURSDAY 06/28/2018.

Attached is the ad used in last years calendar. A few notes on this...
**. This is by no means the model to follow.
Please be creative and do what makes more sense marketing wise.
1. Need to update the color scheme which corresponds to the new website at morvanlegal.net
2. The "MORVAN LEGAL | STANDING FIRM FOR YOUR FUTURE" should be put at the top and made larger
3. "KNOWN AND TRUSTED IN OUR COMMUNITY FOR OVER 21 YEARS" should be changed to "KNOWN AND TRUSTED IN OUR COMMUNITY FOR OVER 22 YEARS"
4. "Dorian K. Morvan, Esq." should be made larger and better positioned.
5. Under the list of practices, it should be changed to have:
"Personal Injury, Legal Malpractice, Unlicensed Contractors, Medical Malpractice, Civil Litigation"
6. Contact information (i.e. contact number, website, and address) should be better positioned
7. Placement of endorsement logos should stand out more.
8. New picture of head attorney is attached.

Last but not least... Give it your best shot!

```html
<!DOCTYPE html>
<html lang="en">
<head>
<meta charset="utf-8">
<title>Morvan Legal – Calendar Ad</title>
<link rel="stylesheet" href="https://fonts.googleapis.com/css2?family=Montserrat:wght@300;400;600;700&family=Playfair+Display:ital,wght@0,600;0,700;1,400&display=swap">
<style>
  :root {
    --ink: #141414;
    --ink-soft: #2a2a2a;
    --gold: #c9a063;
    --gold-deep: #a8804a;
    --white: #ffffff;
    --paper: #f7f7f5;
    --muted: #555555;
  }
  * { box-sizing: border-box; margin: 0; padding: 0; }
  html, body { width: 1200px; height: 798px; overflow: hidden; background: var(--paper); }
  .ad {
    position: relative; width: 1200px; height: 798px; background: var(--white);
    font-family: "Montserrat", Arial, sans-serif; color: var(--white);
  }
  .promo-panel {
    position: absolute; left: 0; top: 0; width: 520px; height: 710px;
    background: linear-gradient(160deg, #3a3a3a 0%, #1e1e1e 45%, var(--ink) 100%);
    padding: 44px 44px 0 44px;
  }
  .brand { display: flex; align-items: center; gap: 14px; }
  .brand-mark { width: 44px; height: 44px; background: var(--gold); }
  .brand-name { font-size: 30px; font-weight: 600; color: var(--gold); letter-spacing: 1px; line-height: 1; }
  .brand-tagline { font-size: 11px; letter-spacing: 2px; color: var(--white); margin-top: 10px; font-weight: 400; }
  .headline {
    font-family: "Playfair Display", Georgia, serif; font-weight: 700;
    font-size: 42px; line-height: 1.08; margin-top: 28px; text-transform: uppercase;
  }
  .practice-list { list-style: none; margin-top: 24px; width: 432px; }
  .practice-item {
    display: flex; align-items: center; gap: 10px; height: 34px;
    font-size: 18px; font-weight: 600; white-space: nowrap;
  }
  .tick { width: 20px; height: 20px; flex: none; }
  .leader { flex: 1; min-width: 20px; height: 1px; background: rgba(255,255,255,0.55); }
  .thumb {
    width: 68px; height: 38px; border: 2px solid var(--white);
    background: linear-gradient(135deg, #d8b07a, #7a5a3a);
    flex: none;
  }
  .practice-item:nth-child(1) .thumb { margin-right: 96px; }
  .practice-item:nth-child(2) .thumb { margin-right: 72px; }
  .practice-item:nth-child(3) .thumb { margin-right: 48px; }
  .practice-item:nth-child(4) .thumb { margin-right: 24px; }
  .practice-item:nth-child(5) .thumb { margin-right: 0; }
  .cta-band {
    position: absolute; left: 0; bottom: 0; width: 520px; height: 150px;
    background: var(--ink); padding: 20px 44px;
  }
  .cta {
    font-family: "Playfair Display", Georgia, serif; font-weight: 700; font-size: 24px;
  }
  .cta u { text-decoration-thickness: 2px; text-underline-offset: 4px; }
  .contact-row { display: flex; align-items: center; gap: 14px; margin-top: 12px; }
  .contact-icon { width: 30px; height: 30px; background: var(--gold); display: flex; align-items: center; justify-content: center; flex: none; }
  .phone { font-size: 30px; font-weight: 300; line-height: 1; }
  .web { font-size: 22px; font-weight: 400; color: var(--gold); letter-spacing: 3px; text-transform: uppercase; }
  .attorney-photo {
    position: absolute; left: 520px; top: 0; width: 680px; height: 640px;
    background: radial-gradient(circle at 60% 35%, #e8d6b8 0%, #b9a48a 30%, #6e6258 65%, #3f3a36 100%);
  }
  .attorney-bar {
    position: absolute; left: 720px; top: 568px; width: 450px; height: 52px;
    background: rgba(20,20,20,0.88); border-radius: 26px 0 0 26px;
    display: flex; align-items: center; gap: 14px; padding-left: 30px;
  }
  .attorney-role { font-size: 15px; letter-spacing: 3px; font-weight: 400; }
  .attorney-name { font-family: "Playfair Display", Georgia, serif; font-style: italic; font-size: 22px; color: var(--gold); white-space: nowrap; }
  .endorsements {
    position: absolute; left: 520px; top: 640px; width: 680px; height: 70px;
    display: flex; align-items: center; justify-content: flex-end; gap: 30px; padding-right: 40px;
    background: var(--white);
  }
  .badge { width: 46px; height: 46px; background: var(--gold-deep); }
  .badge.round { border-radius: 50%; }
  .badge.wide { width: 60px; height: 30px; }
  .address-strip {
    position: absolute; left: 0; top: 710px; width: 1200px; height: 88px;
    background: var(--white); display: flex; align-items: center; gap: 14px; padding-left: 44px;
    border-top: 1px solid #e3e3e3;
  }
  .address { font-size: 16px; letter-spacing: 1.5px; color: var(--muted); text-transform: uppercase; }
</style>
</head>
<body>
<main class="ad">
  <section class="promo-panel">
    <div class="brand">
      <div class="brand-mark"></div>
      <div class="brand-name">MORVAN LEGAL</div>
    </div>
    <p class="brand-tagline">STANDING FIRM FOR YOUR FUTURE</p>

    <h1 class="headline">Known and trusted in our community for over 22 years</h1>

    <ul class="practice-list">
      <li class="practice-item">
        <svg class="tick" viewBox="0 0 20 20"><circle cx="10" cy="10" r="10" fill="#c9a063"/><path d="M5.5 10.5l3 3 6-6.5" stroke="#141414" stroke-width="2.2" fill="none"/></svg>
        Personal Injury<span class="leader"></span>
        <div class="thumb" role="img" aria-label="Photo of an injury being tended"></div>
      </li>
      <li class="practice-item">
        <svg class="tick" viewBox="0 0 20 20"><circle cx="10" cy="10" r="10" fill="#c9a063"/><path d="M5.5 10.5l3 3 6-6.5" stroke="#141414" stroke-width="2.2" fill="none"/></svg>
        Legal Malpractice<span class="leader"></span>
        <div class="thumb" role="img" aria-label="Photo of a legal document being signed"></div>
      </li>
      <li class="practice-item">
        <svg class="tick" viewBox="0 0 20 20"><circle cx="10" cy="10" r="10" fill="#c9a063"/><path d="M5.5 10.5l3 3 6-6.5" stroke="#141414" stroke-width="2.2" fill="none"/></svg>
        Unlicensed Contractors<span class="leader"></span>
        <div class="thumb" role="img" aria-label="Photo of construction tools"></div>
      </li>
      <li class="practice-item">
        <svg class="tick" viewBox="0 0 20 20"><circle cx="10" cy="10" r="10" fill="#c9a063"/><path d="M5.5 10.5l3 3 6-6.5" stroke="#141414" stroke-width="2.2" fill="none"/></svg>
        Medical Malpractice<span class="leader"></span>
        <div class="thumb" role="img" aria-label="Photo of medical equipment"></div>
      </li>
      <li class="practice-item">
        <svg class="tick" viewBox="0 0 20 20"><circle cx="10" cy="10" r="10" fill="#c9a063"/><path d="M5.5 10.5l3 3 6-6.5" stroke="#141414" stroke-width="2.2" fill="none"/></svg>
        Civil Litigation<span class="leader"></span>
        <div class="thumb" role="img" aria-label="Photo of a contract on a desk"></div>
      </li>
    </ul>

    <div class="cta-band">
      <p class="cta">Call Today for A <u>Free</u> Consultation</p>
      <div class="contact-row">
        <span class="contact-icon">
          <svg width="18" height="18" viewBox="0 0 24 24"><path d="M6.6 10.8a15.1 15.1 0 006.6 6.6l2.2-2.2c.3-.3.7-.4 1-.2 1.1.4 2.3.6 3.6.6.6 0 1 .4 1 1V20c0 .6-.4 1-1 1A17 17 0 013 4c0-.6.4-1 1-1h3.5c.6 0 1 .4 1 1 0 1.3.2 2.5.6 3.6.1.3 0 .7-.2 1z" fill="#141414"/></svg>
        </span>
        <span class="phone">(888)-555-0142</span>
      </div>
      <div class="contact-row">
        <span class="contact-icon">
          <svg width="18" height="18" viewBox="0 0 24 24" fill="none" stroke="#141414" stroke-width="2"><circle cx="12" cy="12" r="9"/><path d="M3 12h18M12 3c3 3 3 15 0 18M12 3c-3 3-3 15 0 18"/></svg>
        </span>
        <span class="web">morvanlegal.net</span>
      </div>
    </div>
  </section>

  <div class="attorney-photo" role="img" aria-label="Portrait photo of attorney Dorian K. Morvan in a grey suit in his office"></div>
  <div class="attorney-bar">
    <span class="attorney-role">ATTORNEY</span>
    <span class="attorney-name">Dorian K. Morvan, Esq.</span>
  </div>

  <div class="endorsements" aria-label="Endorsements">
    <div class="badge wide"></div>
    <div class="badge round"></div>
    <div class="badge"></div>
    <div class="badge wide"></div>
    <div class="badge round"></div>
  </div>

  <footer class="address-strip">
    <span class="contact-icon">
      <svg width="16" height="18" viewBox="0 0 24 24"><path d="M12 2a7 7 0 00-7 7c0 5 7 13 7 13s7-8 7-13a7 7 0 00-7-7zm0 9.5A2.5 2.5 0 1112 6.5a2.5 2.5 0 010 5z" fill="#ffffff"/></svg>
    </span>
    <span class="address">2180 Larchmont Ave., Suite #415 Beverly Hills, CA 90210</span>
  </footer>
</main>
</body>
</html>
```